Business card for Financial Technology company

Hello! We'd like to create business cards for 4 members of our company. Our company is a financial technology business that provides funding for businesses. We want to give it a VC (venture captal) look and feel. Clean, fresh and minimal but with a flair of artistry. I'll include some samples of cards we like. It would be great if the back of the card was artistic (see sample files 1 and 2) and the front of the card was the business info. The name of the company is Q8 Funding.

```html
<!DOCTYPE html>
<html lang="en">
<head>
<meta charset="utf-8">
<title>Q8 Funding – Business Card</title>
<link href="https://fonts.googleapis.com/css2?family=Poppins:wght@400;500&display=swap" rel="stylesheet">
<style>
  :root {
    --backdrop: #1c1c1c;
    --card-white: #ffffff;
    --brand-green: #2e9a47;
    --ink: #2b2b2b;
    --rule: #9a9a9a;
    --back-text: #ffffff;
    --mosaic-pink: #e3257a;
    --mosaic-purple: #7a2a8c;
    --mosaic-teal: #136b5e;
    --mosaic-orange: #f48a3c;
    --mosaic-blue: #2fa9e0;
  }
  html, body {
    margin: 0;
    padding: 0;
    width: 1093px;
    height: 1200px;
    overflow: hidden;
    background: var(--backdrop);
    font-family: "Poppins", sans-serif;
  }
  .canvas {
    position: relative;
    width: 1093px;
    height: 1200px;
  }
  .card {
    position: absolute;
    left: 264px;
    width: 580px;
    height: 357px;
    overflow: hidden;
  }
  .card-front {
    top: 226px;
    background: var(--card-white);
  }
  .card-back {
    top: 620px;
  }

  /* Front */
  .brand-name {
    position: absolute;
    left: 60px;
    top: 160px;
    display: flex;
    align-items: center;
    gap: 8px;
    font-weight: 500;
    font-size: 26px;
    color: var(--brand-green);
    line-height: 1;
  }
  .brand-name .brand-square {
    width: 14px;
    height: 14px;
    background: var(--brand-green);
  }
  .divider {
    position: absolute;
    left: 289px;
    top: 75px;
    width: 1px;
    height: 208px;
    background: var(--rule);
  }
  .details {
    position: absolute;
    left: 307px;
    top: 88px;
    color: var(--ink);
  }
  .person-name {
    margin: 0;
    font-weight: 500;
    font-size: 24px;
    line-height: 1;
    color: var(--brand-green);
  }
  .person-role {
    margin: 1px 0 0;
    font-weight: 400;
    font-size: 17px;
    line-height: 1.1;
  }
  .contact-list {
    list-style: none;
    margin: 14px 0 0;
    padding: 0;
  }
  .contact-list li {
    display: flex;
    align-items: center;
    gap: 6px;
    font-size: 17px;
    line-height: 21px;
  }
  .contact-list svg {
    width: 16px;
    height: 16px;
    flex: none;
  }
  .address {
    margin: 12px 0 0;
    font-size: 17px;
    line-height: 21px;
    font-style: normal;
  }

  /* Back */
  .mosaic {
    position: absolute;
    inset: 0;
    background:
      linear-gradient(135deg, var(--mosaic-pink) 0%, var(--mosaic-orange) 20%, transparent 40%),
      linear-gradient(225deg, var(--brand-green) 0%, var(--mosaic-teal) 22%, transparent 45%),
      linear-gradient(45deg, var(--mosaic-purple) 0%, var(--mosaic-pink) 45%, var(--mosaic-purple) 100%);
  }
  .mosaic::after {
    content: "";
    position: absolute;
    left: 70px;
    top: 100px;
    width: 120px;
    height: 120px;
    background: radial-gradient(circle, var(--mosaic-blue) 0%, transparent 70%);
    opacity: 0.6;
  }
  .back-name {
    position: absolute;
    left: 0;
    right: 0;
    top: 156px;
    text-align: center;
    color: var(--back-text);
    font-weight: 500;
    font-size: 38px;
    line-height: 44px;
  }
</style>
</head>
<body>
<main class="canvas">
  <section class="card card-front">
    <div class="brand-name"><span class="brand-square"></span>Q8 Funding</div>
    <div class="divider"></div>
    <div class="details">
      <h1 class="person-name">Daniel Reeves</h1>
      <p class="person-role">Managing Director</p>
      <ul class="contact-list">
        <li>
          <svg viewBox="0 0 24 24" aria-hidden="true"><path fill="var(--brand-green)" d="M6.6 10.8a15 15 0 0 0 6.6 6.6l2.2-2.2a1 1 0 0 1 1-.25 11.4 11.4 0 0 0 3.6.57 1 1 0 0 1 1 1V20a1 1 0 0 1-1 1A17 17 0 0 1 3 4a1 1 0 0 1 1-1h3.5a1 1 0 0 1 1 1c0 1.25.2 2.45.57 3.57a1 1 0 0 1-.25 1z"/><path fill="none" stroke="var(--brand-green)" stroke-width="1.8" d="M14 3a7 7 0 0 1 7 7M14 6.5a3.5 3.5 0 0 1 3.5 3.5"/></svg>
          021-480 317 562
        </li>
        <li>
          <svg viewBox="0 0 24 24" aria-hidden="true"><rect x="2" y="5" width="20" height="14" fill="var(--brand-green)"/><path fill="none" stroke="#fff" stroke-width="1.6" d="M2 5l10 8 10-8M2 19l7-6M22 19l-7-6"/></svg>
          hello@q8funding.com
        </li>
        <li>
          <svg viewBox="0 0 24 24" aria-hidden="true"><g fill="none" stroke="var(--brand-green)" stroke-width="1.8"><circle cx="12" cy="12" r="9.5"/><ellipse cx="12" cy="12" rx="4" ry="9.5"/><path d="M2.5 12h19M4 7h16M4 17h16"/></g></svg>
          www.q8funding.com
        </li>
      </ul>
      <address class="address">421, Address line goes here<br>45452,Country Name</address>
    </div>
  </section>

  <section class="card card-back">
    <div class="mosaic" role="img" aria-label="Colourful geometric mosaic of triangles in pink, purple, orange, green and blue"></div>
    <p class="back-name">Q8 Funding</p>
  </section>
</main>
</body>
</html>
```